Inspiring Poster for Company Staff Room

What we need:
We want an awesome design to create a poster that will be plaque mounted in our staff room. We just went through a very motivating workshop to discover our "WHY" as a company...basically, to define the reason we are in business, and to define what motivates us to come to work every day. The poster must be motivating but really resonate with our team…we are not looking for a “typical” motivational poster that we can purchase off Amazon!

Who we are:
We are a property management company, a team of 20 that is passionate about our investors, and residents who rent from us, but more importantly, we love helping people and making a difference in our industry. We are proud and work hard for every single 5 star Google review we achieve.

Information for you:
We have included a mock up of the poster, which words we want, and the placement of them (in a general sense) but we need a designer to really bring this together in an inspiring poster that represents our company’s culture, feel, and fit. We have also included a logo file, as well as examples of our business cards, letterhead and thank you card already designed.
Here are the parameters:

(1) Poster size: 24” x 36”
(2) Full colour
(3) Must incorporate our company logo
(4) Must incorporate the following words:

Why do I come to work?

“To feel fulfilled by empathizing, educating and empowering our clients and co-workers so that we can build strong, impactful relationships”

Own the outcome

(5) Please see our website at www.brindlecovepm.com to get a feel for our company culture and for a better idea of our current company graphics

Target Market(s)

Our staff. Will not be seen by our clients

Industry/Entity Type

Real Estate

Font styles to use
Serif
Sans Serif

Requirements
Should not have
• Would not want this to be too "busy." if you can picture it, the poster will be mounted on the wall as soon as someone enters the room. The idea is to remind them each day why they come to work.

```html
<!DOCTYPE html>
<html lang="en">
<head>
<meta charset="utf-8">
<title>Why Do I Come to Work – Staff Room Poster</title>
<link rel="stylesheet" href="https://fonts.googleapis.com/css2?family=Montserrat:ital,wght@0,700;0,800;0,900;1,900&family=Questrial&display=swap">
<style>
  :root {
    --brand-blue: #29a8e8;
    --brand-blue-light: #5fc0f2;
    --brand-blue-deep: #1b8fcf;
    --charcoal: #333333;
    --charcoal-light: #7a7a7a;
    --paper: #ffffff;
    --paper-shade: #e6e6e6;
  }
  * { margin: 0; padding: 0; box-sizing: border-box; }
  html, body {
    width: 872px; height: 1200px; overflow: hidden;
    background: var(--paper);
  }
  .poster {
    position: relative; width: 872px; height: 1200px; overflow: hidden;
    background: linear-gradient(135deg, var(--brand-blue-light), var(--brand-blue) 55%, var(--brand-blue-deep));
  }
  .poster-sheet {
    position: absolute; left: 24px; top: 23px; width: 824px; height: 1158px;
    background: linear-gradient(160deg, var(--paper) 40%, var(--paper-shade));
    overflow: hidden;
  }
  .poster-shapes { position: absolute; inset: 0; }

  .brand {
    position: absolute; left: 0; top: 82px; width: 824px;
    display: flex; align-items: center; justify-content: center; gap: 18px;
  }
  .brand-mark { width: 64px; height: 64px; background: var(--brand-blue); }
  .brand-name {
    font-family: "Montserrat", sans-serif; font-weight: 800;
    color: var(--brand-blue); text-transform: uppercase; line-height: 1;
  }
  .brand-name-main { display: block; font-size: 44px; letter-spacing: 2px; }
  .brand-name-sub { display: block; font-size: 15px; letter-spacing: 5.4px; margin-top: 8px; }

  .headline-band {
    position: absolute; left: 0; top: 264px; width: 824px; height: 158px;
    background: linear-gradient(100deg, var(--charcoal-light), #3c3c3c);
    display: flex; align-items: center; justify-content: center;
  }
  .headline-why {
    font-family: "Montserrat", sans-serif; font-weight: 900;
    font-size: 142px; line-height: 1; color: var(--paper); letter-spacing: 2px;
    transform: scaleY(1.02);
  }
  .question-band {
    position: absolute; left: 0; top: 423px; width: 824px; height: 98px;
    background: linear-gradient(90deg, var(--brand-blue-light), var(--brand-blue) 60%, var(--brand-blue-deep));
    display: flex; align-items: center; justify-content: center;
  }
  .question-text {
    font-family: "Montserrat", sans-serif; font-weight: 800;
    font-size: 45px; color: var(--paper); letter-spacing: 1px;
  }

  .purpose {
    position: absolute; left: 40px; top: 646px; width: 744px;
    font-family: "Questrial", sans-serif; font-style: italic;
    font-size: 36px; line-height: 61px; letter-spacing: 1.6px;
    text-align: center; color: var(--brand-blue);
    transform: translateY(-44px);
  }
  .quote-mark {
    position: absolute; font-family: "Montserrat", sans-serif; font-weight: 900;
    font-size: 40px; line-height: 1; color: var(--brand-blue);
  }
  .quote-open { left: 36px; top: 608px; }
  .quote-close { left: 732px; top: 887px; }

  .motto {
    position: absolute; left: 0; top: 1030px; width: 824px; text-align: center;
    font-family: "Montserrat", sans-serif; font-weight: 900; font-style: italic;
    font-size: 33px; letter-spacing: 0.5px; color: var(--charcoal); text-transform: uppercase;
  }
</style>
</head>
<body>
  <main class="poster">
    <section class="poster-sheet">
      <svg class="poster-shapes" width="824" height="1158" viewBox="0 0 824 1158" aria-hidden="true">
        <polygon class="pointer-arrow" points="367,536 457,536 412,572" fill="var(--brand-blue)"/>
        <polygon class="footer-corner-left" points="0,1018 211,1149 170,1158 0,1158" fill="var(--charcoal)"/>
        <polygon class="footer-corner-right" points="824,1021 618,1149 655,1158 824,1158" fill="var(--charcoal)"/>
        <polygon class="footer-chevron" points="170,1158 211,1149 412,1099 618,1149 655,1158" fill="var(--brand-blue)"/>
      </svg>

      <header class="brand">
        <span class="brand-mark"></span>
        <span class="brand-name">
          <span class="brand-name-main">Brindle Cove</span>
          <span class="brand-name-sub">Property Management</span>
        </span>
      </header>

      <div class="headline-band"><h1 class="headline-why">WHY</h1></div>
      <div class="question-band"><h2 class="question-text">do I come to work?</h2></div>

      <span class="quote-mark quote-open">&ldquo;</span>
      <p class="purpose">To feel fulfilled by empathizing,<br>educating and empowering<br>our clients and co-workers so<br>that we can build strong,<br>impactful relationships.</p>
      <span class="quote-mark quote-close">&ldquo;</span>

      <p class="motto">Own the Outcome</p>
    </section>
  </main>
</body>
</html>
```